Website design for online service business

The company provides the following services:
1 - consultancy services on existing products (like tallydesk and brisk 354)
2 - Coaching services - Coach someone on services like using/developing features with existing products, or teach how to be more productive, or improve their business using automation, etc
3 - Training
- Online training on demand on existing products via vokra (like in Tallydesk and brisk 365)
- Online courses through videos lessons and scripts by offering information products where people will need to register and pay in advance to access the online course. (productivity courses for example)

- The goal is for clients to book time with me for one of those areas without too many clicks.
- Clients will be able to Book time using an integration (it would be good to have the layout integrated with the site.) with this https://planner.brisk-suite.example/owa/calendar/BrightKelpStudio1@brightkelpstudio.bookhub.example/bookings/

- there will be areas for which i whish to build a VIP mailing list. It's referenced on the wireframes

References:
https://www.lanternfieldnotes.example/about/about-dorvan/
https://www.pebblecompass.example/
https://tallydeskguide.example/

Target Market(s)

- Small businesses
- Freelancers

Industry/Entity Type

Business

Number of Pages Required

5+ page

Font styles to use
Sans Serif

Colors

Designer to choose colors to be used in the design.

Requirements
Must have
• Must have the design optimized to the less clicks possible to achieve any action
• The colors of the site should follow the logo (provided in attach)
• It should use other color that belong to the same pallet of colors
• Should contain colors that incentivizes people to click and book something
• Images and backgrounds should be made available
• All images sizes and colors should be provided to be able to develop the site according to the design
Nice to have
• The bookings for the time should be integrated within the design. If not possible a redirection to it can work as well.
Should not have
• Links to social media
• Pop-ups
• Intrusive navigations (like navigation bares on the left or right hand side)
• Should not be a template used by many people

```html
<!DOCTYPE html>
<html lang="en">
<head>
<meta charset="utf-8">
<title>Brightkelp Studio – Home</title>
<link href="https://fonts.googleapis.com/css2?family=Arimo:wght@400;700&display=swap" rel="stylesheet">
<style>
:root{
  --orange:#f7931e;
  --blue:#0a76a8;
  --blue-dark:#075f88;
  --ink:#1a1a1a;
  --muted:#333;
  --white:#fff;
  --line:rgba(255,255,255,.75);
  --grey-card:#ececec;
}
*{box-sizing:border-box;margin:0;padding:0}
html,body{width:1200px;height:2284px;overflow:hidden}
body{position:relative;background:var(--white);font-family:"Arimo",Arial,sans-serif;color:var(--ink)}
.abs{position:absolute}
.btn{position:absolute;display:flex;align-items:center;justify-content:center;font-weight:700;font-size:12px;text-transform:uppercase;letter-spacing:.2px;text-decoration:none}
.btn--orange{background:var(--orange);color:var(--white)}
.btn--blue{background:var(--blue);color:var(--white)}
.btn--white{background:var(--white);color:var(--blue)}

/* header */
.site-header{left:0;top:0;width:1200px;height:94px;background:var(--white)}
.brand{display:flex;align-items:center;gap:8px}
.brand__mark{width:18px;height:18px;background:var(--blue)}
.brand__name{font-weight:700;font-size:18px;letter-spacing:1px;color:var(--blue);text-transform:uppercase}
.site-header .brand{position:absolute;left:99px;top:34px}
.main-nav a{position:absolute;top:40px;font-size:13.5px;color:var(--ink);text-decoration:none;text-transform:uppercase}
.main-nav a.is-active{color:var(--orange)}
.main-nav .active-bar{position:absolute;left:503px;top:89px;width:44px;height:3px;background:var(--orange)}

/* hero */
.hero{left:0;top:94px;width:1200px;height:473px}
.hero__photo{position:absolute;inset:0;background:linear-gradient(100deg,#5a4a5a 0%,#8b7a72 35%,#a58f7c 55%,#6d6660 80%,#4f5052 100%)}
.hero__title{position:absolute;left:0;top:168px;width:1200px;text-align:center;color:var(--white);font-size:27.5px;line-height:34px}
.hero .btn{left:518px;top:259px;width:169px;height:38px;font-size:13px}
.live-chat{position:absolute;left:1046px;top:306px;width:68px;height:68px;border-radius:50%;background:rgba(200,200,200,.85);color:var(--white);font-size:12px;font-weight:700;text-align:center;line-height:18px;padding-top:16px}

/* search */
.course-search{left:0;top:567px;width:1200px;height:76px;background:var(--blue)}
.course-search__label{position:absolute;left:120px;top:18px;color:var(--white);text-transform:uppercase}
.course-search__label small{display:block;font-size:10px;font-weight:700}
.course-search__label strong{display:block;font-size:22px;font-weight:400;line-height:24px}
.field{position:absolute;top:16px;height:41px;background:var(--white);color:#999;font-size:12px;padding:12px 13px}
.course-search .btn{left:923px;top:16px;width:160px;height:41px;font-size:13px}

/* about */
.section-title{position:absolute;left:0;width:1200px;text-align:center;color:var(--orange);font-size:17px;text-transform:uppercase}
.section-text{position:absolute;left:0;width:1200px;text-align:center;font-size:11px;line-height:22px;color:var(--muted)}

/* details */
.details{left:0;top:934px;width:1200px;height:336px}
.details__photo{position:absolute;inset:0;background:linear-gradient(90deg,#3d5058 0%,#8e7c70 30%,#4d6d7a 55%)}
.details__shape{position:absolute;left:0;top:0}
.details h3{position:absolute;left:672px;top:48px;color:var(--white);font-size:16px}
.details label{position:absolute;left:670px;color:var(--white);font-size:12px}
.details .rule{position:absolute;left:670px;width:355px;height:1px;background:var(--line)}
.details .btn{left:670px;top:240px;width:177px;height:35px;font-size:11px}

/* courses */
.course-card{position:absolute;top:1462px;width:217px;height:260px}
.course-card__photo{position:absolute;left:0;top:0;width:217px;height:216px}
.course-card__bar{position:absolute;left:0;top:216px;width:217px;height:44px;background:var(--grey-card)}
.course-card__name{position:absolute;left:13px;top:15px;font-size:11px;color:var(--ink)}
.course-card .btn{left:144px;top:0;width:73px;height:44px;font-size:11px}

/* testimonials */
.testimonials{left:0;top:1850px;width:1200px;height:434px}
.testimonials__photo{position:absolute;inset:0;background:linear-gradient(100deg,#3b3530 0%,#5b5046 40%,#4a423a 70%,#3a3632 100%)}
.testimonials h2{position:absolute;left:0;top:50px;width:1200px;text-align:center;color:var(--white);font-size:16px;font-weight:700}
.avatar{position:absolute;left:502px;top:107px;width:86px;height:86px;border-radius:50%;background:radial-gradient(circle,#d9a88a,#8a6a5a);border:3px solid var(--white)}
.testimonial__name{position:absolute;left:602px;top:166px;color:var(--orange);font-size:11px;font-weight:700}
.testimonial__quote{position:absolute;left:0;top:208px;width:1200px;text-align:center;color:var(--white);font-size:10.5px;line-height:23px}
.quote-mark{position:absolute;color:var(--white);font-size:30px;font-weight:700}
.quote-mark--close{position:relative;font-size:18px;font-weight:700;margin-left:8px;top:-3px}

/* footer */
.site-footer{left:0;top:2130px;width:1200px;height:154px}
.footer-nav a{position:absolute;top:99px;font-size:13px;font-weight:700;color:var(--white);text-decoration:none;text-transform:uppercase}
.copyright{position:absolute;left:189px;top:125px;font-size:10px;font-weight:700;color:var(--white)}
.site-footer .brand{position:absolute;left:899px;top:98px}
.site-footer .brand__mark{background:var(--white)}
.site-footer .brand__name{color:var(--white);font-size:16px}
</style>
</head>
<body>

<header class="site-header abs">
  <div class="brand"><span class="brand__mark"></span><span class="brand__name">Brightkelp</span></div>
  <nav class="main-nav">
    <a href="#" class="is-active" style="left:503px">Home</a>
    <a href="#" style="left:579px">About Us</a>
    <a href="#" style="left:684px">Services</a>
    <a href="#" style="left:786px">Cources</a>
    <a href="#" style="left:889px">Testimonials</a>
    <a href="#" style="left:1025px">Contact Us</a>
    <span class="active-bar"></span>
  </nav>
</header>

<section class="hero abs">
  <div class="hero__photo" role="img" aria-label="Photo of students studying together in a library"></div>
  <p class="hero__title">Lorem Ipsum is simply dummy text of the printing<br>and typesetting industry. Lorem Ipsum has been the industry's standard</p>
  <a href="#" class="btn btn--orange">Get Started</a>
  <div class="live-chat">LIVE<br>CHAT</div>
</section>

<section class="course-search abs">
  <div class="course-search__label"><small>Search for</small><strong>Any Coueses</strong></div>
  <div class="field" style="left:289px;width:303px">Select your date</div>
  <div class="field" style="left:606px;width:303px">Select your staff</div>
  <a href="#" class="btn btn--orange">Search</a>
</section>

<section class="about">
  <h2 class="section-title" style="top:683px">About Us</h2>
  <p class="section-text" style="top:723px">Lorem Ipsum is simply dummy text of the printing and typesetting industry. Lorem Ipsum has been the industry's<br>standard dummy text ever since the 1500s, when an unknown printer took a galley of type and scrambled it to make a type specimen book.<br>It has survived not only five centuries, but also the leap into electronic typesetting, remaining essentially unchanged.<br>It was popularised in the 1960s with the release of Quillmark sheets containing Lorem Ipsum passages, and more recently<br>with desktop publishing software like Folio Setter including versions of Lorem Ipsum.</p>
  <a href="#" class="btn btn--blue" style="left:533px;top:850px;width:137px;height:35px;font-size:11px">Learn More</a>
</section>

<section class="details abs">
  <div class="details__photo" role="img" aria-label="Photo of a smiling student among classmates"></div>
  <svg class="details__shape" width="1200" height="336" viewBox="0 0 1200 336">
    <polygon points="640,0 658,0 556,336 520,336" fill="var(--blue)" opacity=".85"/>
    <polygon points="658,0 1200,0 1200,336 556,336" fill="var(--orange)"/>
  </svg>
  <h3>ADD YOUR DETAILS :</h3>
  <label style="top:105px">Name :</label>
  <span class="rule" style="top:129px"></span>
  <label style="top:174px">Email :</label>
  <span class="rule" style="top:195px"></span>
  <a href="#" class="btn btn--white">Book Your Course</a>
</section>

<section class="courses">
  <h2 class="section-title" style="top:1329px">Our Courses</h2>
  <p class="section-text" style="top:1369px">Lorem Ipsum is simply dummy text of the printing and typesetting industry. Lorem Ipsum has been the industry's standard<br>dummy text ever since the 1500s, when an unknown printer took a galley of type and scrambled it to make a type specimen book.</p>

  <article class="course-card" style="left:228px">
    <div class="course-card__photo" role="img" aria-label="Photo of a business meeting around a table" style="background:linear-gradient(135deg,#c9cdd2,#8c8580 60%,#b9b2aa)"></div>
    <div class="course-card__bar"><span class="course-card__name">Business course :</span><a href="#" class="btn btn--orange">Book</a></div>
  </article>
  <article class="course-card" style="left:493px">
    <div class="course-card__photo" role="img" aria-label="Illustration of a digital globe and network connections" style="background:radial-gradient(circle at 35% 40%,#7fd3f0,#1b6fa0 55%,#0b2f4e)"></div>
    <div class="course-card__bar"><span class="course-card__name">Technology course :</span><a href="#" class="btn btn--orange">Book</a></div>
  </article>
  <article class="course-card" style="left:758px">
    <div class="course-card__photo" role="img" aria-label="Overhead photo of a team working at a round table" style="background:radial-gradient(circle,#a8a39c,#6f6a64 70%,#55514c)"></div>
    <div class="course-card__bar"><span class="course-card__name">Software course :</span><a href="#" class="btn btn--orange">Book</a></div>
  </article>

  <a href="#" class="btn btn--blue" style="left:533px;top:1767px;width:137px;height:33px;font-size:11px">View More</a>
</section>

<section class="testimonials abs">
  <div class="testimonials__photo" role="img" aria-label="Dimmed photo of students studying in a classroom"></div>
  <h2>TESTIMONIALS</h2>
  <div class="avatar" role="img" aria-label="Portrait of the student giving the testimonial"></div>
  <span class="testimonial__name">SAMANTA ,student</span>
  <span class="quote-mark" style="left:308px;top:172px">“</span>
  <p class="testimonial__quote">Lorem Ipsum is simply dummy text of the printing and typesetting industry. Lorem Ipsum has been the industry's<br>standard dummy text ever since the 1500s, when an unknown printer took a galley of type and scrambled it to make a type specimen book.<br>It has survived not only five centuries, but also the leap into electronic typesetting, remaining essentially unchanged<span class="quote-mark--close">”</span></p>
</section>

<footer class="site-footer abs">
  <svg class="abs" style="left:0;top:0" width="1200" height="154" viewBox="0 0 1200 154">
    <path d="M0,70 C300,92 700,100 900,60 C1030,34 1130,22 1200,30 L1200,154 L0,154 Z" fill="var(--blue)"/>
  </svg>
  <nav class="footer-nav">
    <a href="#" style="left:189px">Home</a>
    <a href="#" style="left:265px">About Us</a>
    <a href="#" style="left:370px">Services</a>
    <a href="#" style="left:474px">Cources</a>
    <a href="#" style="left:576px">Testimonials</a>
    <a href="#" style="left:711px">Contact Us</a>
  </nav>
  <p class="copyright">© 2017 Corvella • Privacy &amp; Cookies</p>
  <div class="brand"><span class="brand__mark"></span><span class="brand__name">Brightkelp</span></div>
</footer>

</body>
</html>
```